8-page brochure for laboratory equipment in the beverage can industry

We are a small company in the quality inspection and testing industry for beverage and food cans and are in need of a product brochure for one of our key products.The brochure should comprise of 8-pages. We will need both a print-ready format (which we would like to print on 2 double-sided A3 pages, then fold them), as well as an electronic version of the brochure (PDF). We also need to be able to make modifications to it, so we will need the open design file.We have corporate colors and fonts that will have to be used, which we will provide you with.The structure and content are defined, but we need some creative thinking to make it look great!

Target Market(s)

Beverage fillers

Font styles to use
Other font styles liked:
• Nexa Bold, Gotham Book, Calibri

Requirements
Must have
• Must be informative and look appealing.
• Must use the content from the Word document provided (better quality images will be provided if needed).
• Must use the company's corporate colors and fonts.
• Colors:
• Green: CMYK 99, 21, 86, 7
• Dark Grey: CMYK 67, 62, 58, 45
• Light Grey: CMYK 45, 36, 35, 1

```html
<!DOCTYPE html>
<html lang="en">
<head>
<meta charset="utf-8">
<title>ClearSight QC – Brochure Spread</title>
<link href="https://fonts.googleapis.com/css2?family=Montserrat:wght@400;500;700;800&display=swap" rel="stylesheet">
<style>
  :root {
    --green: #2a9d6c;
    --dark-grey: #4a3f40;
    --light-grey: #a3a4a6;
    --paper: #f1f1f1;
    --white: #ffffff;
    --accent: #f2e21b;
    --canvas: #d9d9d9;
    --caption: #2a9d6c;
  }
  * { box-sizing: border-box; margin: 0; padding: 0; }
  html, body { width: 1200px; height: 900px; overflow: hidden; }
  body {
    background: var(--canvas);
    font-family: "Montserrat", Arial, sans-serif;
    position: relative;
  }
  .spread {
    position: absolute; left: 50px; top: 61px;
    width: 1100px; height: 778px;
    display: flex;
    box-shadow: 0 6px 24px rgba(0,0,0,.18);
  }
  .page { position: relative; width: 550px; height: 778px; overflow: hidden; }
  .page--software { background: var(--green); color: var(--white); }
  .page--xray { background: var(--dark-grey); color: var(--white); }

  h2.section-title {
    font-weight: 800; text-transform: uppercase; letter-spacing: .02em;
    line-height: 1.12;
  }
  .feature-list { list-style: none; font-size: 9.5px; line-height: 1.35; }
  .feature-list > li { position: relative; padding-left: 14px; margin-bottom: 2px; }
  .feature-list > li::before {
    content: ""; position: absolute; left: 0; top: 3px;
    width: 6px; height: 6px; background: var(--accent);
  }
  .sub-list { list-style: none; font-size: 9.5px; line-height: 1.35; padding-left: 14px; }
  .sub-list li { position: relative; padding-left: 9px; }
  .sub-list li::before { content: "▸"; position: absolute; left: 0; font-size: 8px; top: 1px; }
  h3.edition {
    font-weight: 700; font-size: 16px; margin-bottom: 4px;
    position: relative; padding-left: 14px;
  }
  h3.edition::before {
    content: ""; position: absolute; left: 0; top: 7px;
    width: 6px; height: 6px; background: var(--accent);
  }

  /* Left page */
  .software-intro { position: absolute; left: 36px; top: 120px; width: 230px; }
  .software-intro h2 { font-size: 21px; margin-bottom: 16px; }
  .edition-light { position: absolute; left: 36px; top: 395px; width: 250px; }
  .editions-column {
    position: absolute; left: 290px; top: 70px; width: 235px; height: 420px;
    border-left: 1px solid rgba(255,255,255,.55); padding-left: 14px;
  }
  .edition-block { margin-bottom: 22px; }
  .software-screen {
    position: absolute; left: 150px; top: 540px; width: 380px; height: 210px;
    background: var(--white); padding: 10px;
  }
  .software-screen .fill {
    width: 100%; height: 100%;
    background: linear-gradient(135deg, #e9ecec 0%, #cfd6d3 60%, #8fa59b 100%);
  }

  /* Right page */
  .xray-intro { position: absolute; left: 30px; top: 70px; width: 255px; }
  .xray-intro h2 { font-size: 19px; margin-bottom: 14px; }
  .xray-intro p {
    font-size: 9px; line-height: 1.4; text-align: justify;
    position: relative; padding-left: 14px; margin-bottom: 12px;
  }
  .xray-intro p::before {
    content: ""; position: absolute; left: 0; top: 3px;
    width: 6px; height: 6px; background: var(--accent);
  }
  .image-column {
    position: absolute; left: 305px; top: 70px; width: 245px; height: 360px;
    background: var(--paper); padding: 12px 14px;
  }
  .figure { margin-bottom: 8px; }
  .figure .fill { width: 100%; }
  .figure figcaption { font-size: 7.5px; color: var(--caption); margin-top: 3px; }
  .fill--projection { height: 55px; background: linear-gradient(90deg, #3a4640, #9aa39f); }
  .fill--section { height: 95px; background: linear-gradient(135deg, #3a3a3a, #6e6e6e); }
  .fill--virtual { height: 110px; background: linear-gradient(135deg, #3a3f6e 0%, #c9cbd2 100%); }

  .diagram-panel {
    position: absolute; left: 0; top: 300px; width: 290px; height: 160px;
    background: var(--paper);
  }
  .diagram-panel .fill {
    position: absolute; inset: 12px 30px;
    background: linear-gradient(135deg, #ffffff, #e2e2e2);
    border: 1px solid #cfcfcf;
  }
  .wrinkle-intro { position: absolute; left: 30px; top: 480px; width: 262px; }
  .wrinkle-intro h2 { font-size: 18px; margin-bottom: 10px; }
  .wrinkle-intro .feature-list { font-size: 9px; }
  .wrinkle-panel {
    position: absolute; left: 0; top: 655px; width: 290px; height: 123px;
    background: var(--paper); padding: 12px 20px;
  }
  .wrinkle-panel .fill {
    width: 100%; height: 100%;
    background: linear-gradient(180deg, #e4e4e4, #cfd2d4);
    border: 1px solid #d0d0d0;
  }
  .wrinkle-column {
    position: absolute; left: 305px; top: 455px; width: 245px; height: 323px;
    background: var(--paper); padding: 14px;
  }
  .fill--map {
    height: 170px;
    background: linear-gradient(180deg, #d98a7e 0%, #b8c6e0 100%);
    margin-bottom: 14px;
  }
  .fill--sample {
    height: 105px; width: 150px; margin-left: 65px;
    background: linear-gradient(160deg, #e2e5e7 0%, #c8cac4 100%);
  }
</style>
</head>
<body>
  <main class="spread">

    <section class="page page--software">
      <div class="software-intro">
        <h2 class="section-title">ClearSight QC™ data collection and evaluation software</h2>
        <ul class="feature-list">
          <li>A complete quality control data acquisition solution</li>
          <li>Easy-to-use Statistical Process Control for quick analysis of can inspection data</li>
          <li>Flexible, secure database</li>
          <li>Intuitive inspection reports may be shared and exported</li>
          <li>Track trends and statistics with SPC Graphs</li>
          <li>In use at hundreds of canmakers and canners around the world</li>
          <li>Available in 3 versions: Light – SPC – Pro</li>
        </ul>
      </div>

      <div class="edition-light">
        <h3 class="edition">ClearSight QC™ Light:</h3>
        <ul class="sub-list">
          <li>Universal gauge interface</li>
          <li>Fully-customizable inspections</li>
          <li>Seam images (integrates with JOINTscope)</li>
          <li>Individual operator logins</li>
          <li>Switchable language</li>
          <li>Graphical view of specification limits</li>
          <li>Customizable reports for single test evaluation</li>
        </ul>
      </div>

      <div class="editions-column">
        <div class="edition-block">
          <h3 class="edition">ClearSight QC™ SPC:</h3>
          <ul class="sub-list">
            <li>Basic statistical reporting</li>
            <li>Track trends and statistics with SPC Graphs</li>
            <li>Basic key functionality (Product Code, Can Code etc.)</li>
            <li>Seam control Sheet</li>
            <li>Recheck capabilities</li>
            <li>Data-export</li>
          </ul>
        </div>
        <div class="edition-block">
          <h3 class="edition">ClearSight QC™ Pro:</h3>
          <ul class="sub-list">
            <li>Expanded statistical reporting</li>
            <li>Expanded key functionality (Product Code, Can Code etc.)</li>
            <li>Automatic reporting (E-Mail)</li>
            <li>Views</li>
            <li>Assessment</li>
            <li>Networking</li>
            <li>Scheduled tasks</li>
            <li>Event-triggering</li>
            <li>Dashboard</li>
            <li>Background data-export and import</li>
            <li>Additional read-only License</li>
          </ul>
        </div>
      </div>

      <figure class="software-screen">
        <div class="fill" role="img" aria-label="Screenshot of the CSQ 9 software showing SPC charts, data tables and seam images"></div>
      </figure>
    </section>

    <section class="page page--xray">
      <div class="xray-intro">
        <h2 class="section-title">How does X-ray seam measurement work?</h2>
        <p>X-rays are sent through the seam sideways. A detector reads the remaining radiation. When X-rays are travelling through several layers of material, less radiation is going through the material, meaning that some percentage will be absorbed by the material depending on density. This results in a darker region within the image, which, in turn, allows a precise measurement of the individual layers of the seam.</p>
        <p>For a better understanding and visualization, the virtual seam image translates the X-ray image into a classic cross-section image.</p>
      </div>

      <div class="image-column">
        <figure class="figure">
          <div class="fill fill--projection" role="img" aria-label="Radial X-ray projection of a can seam"></div>
          <figcaption>X-Ray projection (radial)</figcaption>
        </figure>
        <figure class="figure">
          <div class="fill fill--section" role="img" aria-label="Tangential X-ray cross-section of a double seam"></div>
          <figcaption>Classic cross section view (tangential)</figcaption>
        </figure>
        <figure class="figure">
          <div class="fill fill--virtual" role="img" aria-label="Virtual seam drawing with seam height, body hook, cover hook and overlap measurements"></div>
          <figcaption>Conversion of X-Ray image to "virtual seam"</figcaption>
        </figure>
      </div>

      <div class="diagram-panel">
        <div class="fill" role="img" aria-label="Technical diagram of X-ray source and detector passing beams through a can seam"></div>
      </div>

      <div class="wrinkle-intro">
        <h2 class="section-title">Wrinkle rating with X-ray</h2>
        <ul class="feature-list">
          <li>Non-destructive wrinkle measurement</li>
          <li>360° scan of the can seam</li>
          <li>Automatic detection and calculation of tightness percentage</li>
          <li>Number of anomalies in the cover hook are clearly visible</li>
          <li>Leakers will be found thanks to the 360° scan</li>
        </ul>
      </div>

      <div class="wrinkle-panel">
        <div class="fill" role="img" aria-label="Software view of a 360° wrinkle scan"></div>
      </div>

      <div class="wrinkle-column">
        <div class="fill fill--map" role="img" aria-label="Colour-coded wrinkle map of the cover hook"></div>
        <div class="fill fill--sample" role="img" aria-label="Close-up photo of a stripped cover hook sample"></div>
      </div>
    </section>

  </main>
</body>
</html>
```